Awesome business card design needed

We need a new business card design to go with our new logo.
We are a web development agency that specialises in highly complex back-end integrations as opposed to design, our customers are retailers, hotels, hospitals and any other organisation that has a large online marketing department.
Take a look at our website - www.orvekplus.com for some inspiration.
We want our new business cards to exude class, professionalism and style.
We are likely to choose a high-end card to print them on but we want the design of the card itself to really turn heads.
We have no specific colour requirements, the logo as you will see is a turquoise colour R89 G171 B167 #59aba7 but it can also be in white if you want to make the colour of the card something different.
The information on the card should be:
Name
Position
Tel
email
Potentially a double sided card could have our web address, twitter and FB links.

```html
<!DOCTYPE html>
<html lang="en">
<head>
<meta charset="utf-8">
<title>Orvekplus Business Card</title>
<link rel="stylesheet" href="https://fonts.googleapis.com/css2?family=Roboto+Condensed:wght@700&family=PT+Serif&display=swap">
<style>
  :root {
    --page: #e9e6e1;
    --card-dark: #1f1f1f;
    --card-light: #ffffff;
    --teal: #59aba7;
    --teal-deep: #4a9592;
    --teal-faint: #cfe3e2;
    --ink: #111111;
    --bar: #2c2e2c;
    --white: #ffffff;
  }
  * { margin: 0; padding: 0; box-sizing: border-box; }
  html, body { width: 1200px; height: 1000px; overflow: hidden; }
  body { background: var(--page); position: relative; font-family: "PT Serif", serif; }

  .card { position: absolute; box-shadow: 0 6px 14px rgba(0,0,0,.25); overflow: hidden; }

  /* Front */
  .card-front { left: 203px; top: 85px; width: 642px; height: 371px; background: var(--card-dark); }
  .front-accent { position: absolute; left: 0; width: 214px; height: 14px; }
  .front-accent.top { top: 0; }
  .front-accent.bottom { bottom: 0; }
  .front-wordmark {
    position: absolute; left: 287px; top: 132px;
    font-family: "Roboto Condensed", sans-serif; font-weight: 700;
    font-size: 76px; letter-spacing: 1px; line-height: 1; color: var(--white);
  }

  /* Back */
  .card-back { left: 380px; top: 521px; width: 641px; height: 370px; background: var(--card-light); }
  .holder-name {
    position: absolute; left: 39px; top: 22px;
    font-family: "Roboto Condensed", sans-serif; font-weight: 700; font-size: 31px; color: var(--ink); line-height: 1;
  }
  .holder-role {
    position: absolute; left: 40px; top: 59px;
    font-family: "Roboto Condensed", sans-serif; font-weight: 700; font-size: 20px; color: var(--ink); line-height: 1;
  }
  .contact-bars { position: absolute; left: 0; top: 258px; }
  .contact-bars text { font-family: "PT Serif", serif; font-size: 18px; fill: var(--white); }

  .back-wordmark {
    position: absolute; left: 385px; top: 22px; width: 90px; height: 325px;
  }
  .back-wordmark span {
    position: absolute; left: 50%; top: 50%;
    transform: translate(-50%, -50%) rotate(-90deg);
    font-family: "Roboto Condensed", sans-serif; font-weight: 700;
    font-size: 82px; line-height: 1; color: var(--teal-faint); white-space: nowrap;
  }

  .social-column { position: absolute; top: 0; width: 87px; height: 370px; }
  .social-column.first { left: 468px; background: var(--teal-deep); }
  .social-column.second { left: 555px; width: 86px; background: var(--teal); }
  .social-link {
    position: absolute; left: 50%; top: 150px;
    transform: translate(-50%, -50%) rotate(-90deg);
    font-family: "PT Serif", serif; font-size: 21px; color: var(--white); white-space: nowrap;
  }
  .social-mark { position: absolute; left: 18px; top: 301px; width: 45px; height: 45px; }
  .social-mark.light { background: var(--white); }
  .social-mark.dark { background: #2a6f76; border: 2px solid var(--white); left: 13px; }
</style>
</head>
<body>

<section class="card card-front" aria-label="Card front">
  <svg class="front-accent top" viewBox="0 0 214 14" aria-hidden="true"><polygon points="0,0 214,0 200,14 0,14" fill="var(--teal)"/></svg>
  <svg class="front-accent bottom" viewBox="0 0 214 14" aria-hidden="true"><polygon points="0,0 200,0 214,14 0,14" fill="var(--teal)"/></svg>
  <div class="front-wordmark">orvekplus</div>
</section>

<section class="card card-back" aria-label="Card back">
  <div class="holder-name">John Doe</div>
  <div class="holder-role">Your designation</div>

  <svg class="contact-bars" width="300" height="90" viewBox="0 0 300 90">
    <polygon points="0,0 221,0 236,23 0,23" fill="var(--bar)"/>
    <polygon points="0,32 246,32 261,56 0,56" fill="var(--bar)"/>
    <polygon points="0,64 274,64 289,87 0,87" fill="var(--bar)"/>
    <!-- phone icon -->
    <path d="M45 5 c-2 0 -3 2 -2 4 c2 5 6 9 11 11 c2 1 4 0 4 -2 l-3 -3 l-3 2 c-2 -1 -4 -3 -5 -5 l2 -3 z" fill="var(--white)"/>
    <text x="72" y="18">0123456789</text>
    <!-- mail icon -->
    <rect x="43" y="38" width="18" height="13" fill="var(--white)"/>
    <polyline points="43,38 52,46 61,38" fill="none" stroke="var(--bar)" stroke-width="1.5"/>
    <text x="72" y="50">john@orvekplus.com</text>
    <!-- globe icon -->
    <circle cx="52" cy="76" r="7.5" fill="none" stroke="var(--white)" stroke-width="1.4"/>
    <ellipse cx="52" cy="76" rx="3.2" ry="7.5" fill="none" stroke="var(--white)" stroke-width="1.2"/>
    <line x1="44.5" y1="76" x2="59.5" y2="76" stroke="var(--white)" stroke-width="1.2"/>
    <text x="72" y="82">www.orvekplus.com</text>
  </svg>

  <div class="back-wordmark" aria-hidden="true"><span>orvekplus</span></div>

  <div class="social-column first">
    <span class="social-link">friendsnet.com/orvekplus</span>
    <div class="social-mark light"></div>
  </div>
  <div class="social-column second">
    <span class="social-link">chirpline.com/orvekplus</span>
    <div class="social-mark dark"></div>
  </div>
</section>

</body>
</html>
```